Flier Template in Microsoft Word

We need to a have a flier about farm practices developed in Microsoft Word. Each farm will able to add their own logos and photos. We will give them a model that they can customize.

We want a traditional "country" flavor. Green colors and earth tones are best. Please use the photos we have provided.

The final product must be in Microsoft Word for our farmers to customize.
Updates

All designers: Please have a white background (maybe with a watermark). Our client will print these on white paper using a desktop printer. Thank you!

Target Market(s)

People who shop at Farmer's Markets, join CSAs, and enjoy cooking with fresh vegetables.

Industry/Entity Type

Farm

Font styles to use
Serif

Requirements
Must have
• Must use the text and general layout of the Microsoft Word document attached
Must use the pictures we provided.
Final product must be in Microsoft Word
Must be able to easily swap out the logo at the top
Must be able to print on white paper on a desktop printer
Nice to have
• A nice header that looks like a farm or food on the table
A nice watermark or background to make the flier look polished
Should not have
• Do not change the photos
Do not use high tech fonts or graphic treatments

```html
<!DOCTYPE html>
<html lang="en">
<head>
<meta charset="utf-8">
<title>The Growing Series – Sustainable Grazing</title>
<link href="https://fonts.googleapis.com/css2?family=Carlito:ital,wght@0,400;0,700;1,400&display=swap" rel="stylesheet">
<style>
  :root{
    --green-deep:#0b5a14;
    --green-dark:#0e6a1a;
    --green-title:#0a6b1c;
    --green-light:#8cc63f;
    --ink:#1d1d1d;
    --paper:#ffffff;
    --wash:#eef4ea;
  }
  *{box-sizing:border-box;margin:0;padding:0}
  html,body{width:829px;height:1200px;overflow:hidden;background:var(--paper)}
  body{font-family:"Carlito",Calibri,Arial,sans-serif;color:var(--ink);position:relative}
  .flier{position:relative;width:829px;height:1200px;overflow:hidden;background:var(--paper)}
  .backdrop{position:absolute;left:0;top:380px;width:829px;height:560px;
    background:radial-gradient(ellipse at 40% 45%,rgba(200,220,190,.45),rgba(230,240,225,.25) 55%,rgba(255,255,255,0) 75%)}
  .header{position:absolute;left:0;top:0;width:829px;height:125px;
    background:linear-gradient(180deg,#1d7a22 0%,var(--green-deep) 60%,#084a10 100%)}
  .header-stripe{position:absolute;left:0;top:116px;width:829px;height:16px}
  .logo-slot{position:absolute;left:32px;top:43px;width:95px;height:65px;background:var(--paper);
    border:1px solid #000;font-size:14px;line-height:20px;text-align:center;padding-top:6px;color:#000;font-family:Arial,sans-serif}
  .series{position:absolute;left:203px;top:56px;color:#fff}
  .series-name{font-size:21px;font-weight:700;line-height:26px}
  .series-tag{font-size:13px;font-weight:700;line-height:18px}
  .rule{position:absolute;height:2px;background:var(--green-dark)}
  .headline{position:absolute;left:71px;top:168px;width:700px;text-align:center;font-size:33px;font-weight:700;color:var(--green-title);line-height:42px}
  .subhead{position:absolute;left:71px;top:224px;width:700px;text-align:center;font-size:20px;font-style:italic;color:var(--green-title);line-height:28px}
  .section-title{position:absolute;left:74px;font-size:19.5px;font-weight:700;color:var(--green-title);line-height:24px}
  .body-text{position:absolute;left:74px;font-size:15px;line-height:25px;text-align:justify}
  .photo{position:absolute;border:3px solid #fff;box-shadow:0 0 6px rgba(0,0,0,.45)}
  .photo-farmer{left:415px;top:276px;width:354px;height:229px;background:linear-gradient(180deg,#9fb49a 0%,#b6c6a8 30%,#6c9a3c 55%,#4e8a2a 100%)}
  .photo-after{left:73px;top:840px;width:311px;height:233px;background:linear-gradient(180deg,#c7d6e3 0%,#a9b7b6 25%,#8aa650 45%,#6b8a34 75%,#857a3e 100%)}
  .photo-before{left:455px;top:840px;width:311px;height:233px;background:linear-gradient(180deg,#c9d7e4 0%,#9fae9c 28%,#7ea24a 48%,#6f8e3a 70%,#6f6a48 100%)}
  .tag{position:absolute;top:1034px;height:28px;background:#fff;font-size:17px;line-height:28px;color:var(--ink)}
  .tag-after{left:304px;width:72px;padding-left:20px;clip-path:polygon(14px 0,100% 0,100% 100%,14px 100%,0 50%)}
  .tag-before{left:460px;width:78px;padding-left:10px;clip-path:polygon(0 0,calc(100% - 14px) 0,100% 50%,calc(100% - 14px) 100%,0 100%)}
  .footer{position:absolute;left:0;top:1110px;width:829px;height:90px;
    background:linear-gradient(180deg,#0e6a1a 0%,var(--green-deep) 60%,#084a10 100%)}
  .footer-stripe{position:absolute;left:0;top:1104px;width:829px;height:16px}
  .partner-mark{position:absolute;left:32px;top:1120px;width:88px;height:72px;background:#fff;
    display:flex;align-items:center;justify-content:center;text-align:center;font-size:11px;line-height:13px;color:var(--green-dark);padding:4px}
  .footer-text{position:absolute;left:164px;top:1128px;width:620px;color:#fff;font-size:14.5px;line-height:26px}
</style>
</head>
<body>
<div class="flier">
  <div class="backdrop" role="img" aria-label="Faint watermark of a tree over rolling green hills"></div>

  <header class="header"></header>
  <svg class="header-stripe" viewBox="0 0 829 16" preserveAspectRatio="none">
    <polygon points="160,2 829,2 829,14 172,14" fill="var(--green-light)"/>
  </svg>
  <div class="logo-slot">FARM<br>LOGO</div>
  <div class="series">
    <div class="series-name">The Growing Series</div>
    <div class="series-tag">A Healthier Environment, One Meal At a Time</div>
  </div>

  <div class="rule" style="left:71px;top:162px;width:700px"></div>
  <h1 class="headline">Sustainable Grazing</h1>
  <div class="rule" style="left:71px;top:212px;width:700px"></div>
  <p class="subhead">Happier Cows = Healthier Milk and Cleaner Streams</p>

  <h2 class="section-title" style="top:300px">Who We Are</h2>
  <div class="rule" style="left:71px;top:326px;width:327px"></div>
  <p class="body-text" style="top:328px;width:322px">Maple Hollow Dairy Farm is a third generation dairy farm located on 64 acres in the Willow Creek Valley. We raise holsteins to produce milk and also raise hens for eggs. We sell much of our milk, as well as cheese, yogurt and baked goods directly from the farm.</p>

  <div class="photo photo-farmer" role="img" aria-label="Photo of the farmer standing in front of a red tractor in a green field"></div>

  <h2 class="section-title" style="top:497px">What Have We Done</h2>
  <div class="rule" style="left:71px;top:523px;width:327px"></div>
  <p class="body-text" style="top:525px;width:695px">At Maple Hollow Dairy Farm, we take care of our animals and our animals help us take care of the land. Corn and other grains are not a natural part of a cows’ diet, so we don’t feed them that. Instead, we let them roam the pastures eating grass and other plants. We move the cows from pasture to pasture on a thoughtful schedule to prevent overgrazing, and this reduces soil erosion and water pollution. Our animals are happier and our land and water is healthier.</p>

  <h2 class="section-title" style="top:670px">When and Where We Did It</h2>
  <div class="rule" style="left:71px;top:696px;width:700px"></div>
  <p class="body-text" style="top:698px;width:695px">In 2010, we had our cows in a stall barn and corn or soybeans in our fields. We looked into switching some of our acreage from crops to pasture and soon realized that it would beneficial to our cows and our soil. We then installed fencing to divide the fields into smaller paddocks and in spring 2011, we planted a seed mixture containing plants that provide the nutrition our cows need and that provides support for the soil.</p>

  <div class="photo photo-after" role="img" aria-label="After photo: fenced pasture with a grassy, vegetated stream bank"></div>
  <div class="photo photo-before" role="img" aria-label="Before photo: cattle grazing beside an eroded, bare stream bank"></div>
  <div class="tag tag-after">After</div>
  <div class="tag tag-before">Before</div>

  <svg class="footer-stripe" viewBox="0 0 829 16" preserveAspectRatio="none">
    <polygon points="170,2 829,2 829,16 156,16" fill="var(--green-light)"/>
  </svg>
  <footer class="footer"></footer>
  <div class="partner-mark">Riverbend Conservation Council</div>
  <p class="footer-text">Riverbend Conservation Council’s Growing Green Series promotes local farms that produce fresh, high quality, healthy foods using farm practices that keep our water clean and our families safe.</p>
</div>
</body>
</html>
```